Finally a Vodka produced for women ! (Label Design)

We are a small distillery based in Melbourne, Australia and we need a Vodka label design solution that will appeal to women aged 30-50 years and radiate luxury. Full Details are in a design brief attached. We thank you in advance.

Target Market(s)

Affluent females 30-50 years.

Industry/Entity Type

Spirits/Alcohol

Requirements
Must have
• Be clear this is a luxury Vodka.
Nice to have
• Elegance.

```html
<!DOCTYPE html>
<html lang="en">
<head>
<meta charset="utf-8">
<title>Premium Vodka – Rose Quartz Filtered Label</title>
<link rel="stylesheet" href="https://fonts.googleapis.com/css2?family=Playfair+Display:wght@400;700&display=swap">
<style>
  :root {
    --paper: #ffffff;
    --ink: #0d0d0d;
    --rose: #e6b3b8;
    --frame: #cbcbcb;
    --muted: #a6a6a6;
    --ornament: #efefef;
  }
  html, body {
    margin: 0;
    padding: 0;
    width: 1200px;
    height: 1000px;
    overflow: hidden;
    background: var(--paper);
  }
  .canvas {
    width: 1200px;
    height: 1000px;
    display: flex;
    align-items: center;
    justify-content: center;
  }
  .label {
    width: 830px;
    height: 940px;
    display: block;
  }
  .label-frame {
    fill: none;
    stroke: var(--frame);
    stroke-width: 4;
    stroke-linejoin: miter;
  }
  .ornament { fill: var(--ornament); }
  .premium {
    font-family: "Playfair Display", serif;
    font-weight: 700;
    font-size: 38px;
    letter-spacing: 4px;
    fill: var(--ink);
  }
  .product-name {
    font-family: "Playfair Display", serif;
    font-weight: 400;
    font-size: 168px;
    fill: var(--ink);
  }
  .filter-band { fill: var(--rose); }
  .filter-text {
    font-family: "Playfair Display", serif;
    font-weight: 700;
    font-size: 46px;
    fill: var(--paper);
  }
  .origin, .spec {
    font-family: "Playfair Display", serif;
    font-weight: 400;
    fill: var(--muted);
  }
  .origin { font-size: 34px; letter-spacing: 3px; }
  .spec { font-size: 29px; letter-spacing: 1px; }
  .maker {
    font-family: "Playfair Display", serif;
    font-weight: 700;
    fill: var(--ink);
  }
  .maker-name { font-size: 40px; }
  .maker-sub { font-size: 17px; }
</style>
</head>
<body>
<main class="canvas">
  <svg class="label" viewBox="150 270 1050 1200" xmlns="http://www.w3.org/2000/svg" aria-labelledby="label-title">
    <title id="label-title">Premium Vodka, Rose Quartz Filtered – bottle label</title>

    <!-- label outline -->
    <polyline class="label-frame" points="655,386 492,290 341,664 372,690"/>
    <polyline class="label-frame" points="686,398 858,290 1008,664 978,690"/>
    <polyline class="label-frame" points="318,735 160,1121 305,1217 310,1205"/>
    <polyline class="label-frame" points="1032,735 1190,1121 1045,1217 1040,1205"/>
    <polyline class="label-frame" points="420,1290 675,1460 930,1290"/>

    <!-- decorative ornaments -->
    <rect class="ornament" x="585" y="395" width="205" height="155" rx="40" role="img" aria-label="Botanical sprig with leaves and small round blossoms"/>
    <rect class="ornament" x="318" y="692" width="76" height="62" rx="28" role="img" aria-label="Curled scroll flourish"/>
    <rect class="ornament" x="956" y="692" width="76" height="62" rx="28" role="img" aria-label="Curled scroll flourish"/>
    <rect class="ornament" x="275" y="1148" width="280" height="152" rx="60" role="img" aria-label="Leafy scroll flourish"/>
    <rect class="ornament" x="795" y="1148" width="280" height="152" rx="60" role="img" aria-label="Leafy scroll flourish"/>

    <!-- headline -->
    <text class="premium" x="675" y="636" text-anchor="middle">PREMIUM</text>
    <text class="product-name" x="675" y="785" text-anchor="middle" textLength="550" lengthAdjust="spacingAndGlyphs">VODKA</text>

    <!-- rose band -->
    <polygon class="filter-band" points="305,836 1045,836 1087,947 262,947"/>
    <text class="filter-text" x="675" y="908" text-anchor="middle" textLength="636" lengthAdjust="spacing">ROSE QUARTZ FILTERED</text>

    <!-- origin -->
    <text class="origin" x="675" y="1060" text-anchor="middle">Handcrafted in</text>
    <text class="origin" x="675" y="1098" text-anchor="middle">Melbourne, Australia</text>

    <!-- maker -->
    <text class="maker maker-name" x="675" y="1186" text-anchor="middle" textLength="188" lengthAdjust="spacing">SILVER</text>
    <text class="maker maker-name" x="675" y="1228" text-anchor="middle" textLength="188" lengthAdjust="spacing">WREN</text>
    <text class="maker maker-sub" x="675" y="1253" text-anchor="middle" textLength="188" lengthAdjust="spacing">DISTILLERY</text>

    <!-- specification -->
    <text class="spec" x="675" y="1370" text-anchor="middle">40% Alc/Vol</text>
    <text class="spec" x="675" y="1401" text-anchor="middle">700ml</text>
  </svg>
</main>
</body>
</html>
```